Flyer design

I am looking for a design for a double sided flyer. Details of each side as follows.

SIDE 1
Using the 'Keel Lending' logo, also insert 'is your mortgage in good shape?' directly under the logo, (see business cards)

The flyer is to have the following also included:

'Get your Mortgage in shape for Summer'

'Refinance today and potentially receive upwards of $1,500*'

'100% free service'

'Mobile broker to your door, at your convenience'

Call Now 0400 382 947

Email 'oscar@keellending.com.au'

Web www.keellending.com.au

(in smaller writing the following can be written) Re-finance before 2015 and not only will your Mortgage specialist find you a better product, but they will also rebate you 50% of their brokering commission. An average $500,000 loan is likely to result in over $1,500 cash back. Has there ever been a better reason to refinance?

5% of profits donated to our partner bright harbour

SIDE 2
Using the 'Keel Estate Advisory' logo, also insert 'Cutting out the Fatty Commissions' directly under the logo, (see business cards)

'What are you doing with your equity?' (strong emphasis on this statement)

Speak to our investment specialist today and find out how you could potentially use your equity to build a positively geared investment portfolio without spending your own money.

'Your actions today will determine how you live tomorrow'.

Free 1 hour consultation
No selling, just transparent guidance on the in's and out's of property investing along with current hot spots and an analysis of your investment property portfolio potential.

WARNING: beware of typical 'Free' investment seminars where you are ultimately guided down a path to overprized, commission packed, apartments or house and land packages (choked full of

Keel Estate Advisory will not sell you property, only provide transparent guidance so ultimately you can make an informed decision.

It is correct nothing is for free, however, unlike most property investment advisers the only payment/commission Keel Estate Advisory receives is that paid from the bank through brokering the loan on your investment property (should you choose to purchase a property and allow us to broker your loan)

Call today for further information of this amazing offer
Updates

Thanks for your designs so far, I am looking to emphasis the logo's please use them as the main feature, keep it simple, I may need to cut out some of the information so its not too crowded. As well as the logo the other things that need to stand out is the $1,500 rebate and the 'What are you doing with your equity?'. Both these statements and the logo should stand out as soon as someone see the flyer. Feel free to leave out some of the other info if you feel the flyer will look better, I can add to it if need be, but the presentation is vital. Simple is the key. Thanks again. Oscar

Thanks for your designs, I am still considering my options, however, the last 2 posted designs are on the right path. Thanks

Target Market(s)

Middle age, middle income property owners. Generally families.

Industry/Entity Type

Investment

Requirements
Must have
• Please make the 2 logo's the most prominent feature of the flyer

```html
<!DOCTYPE html>
<html lang="en">
<head>
<meta charset="utf-8">
<title>Keel Lending – Refinance Flyer</title>
<link rel="stylesheet" href="https://fonts.googleapis.com/css2?family=PT+Serif:wght@400;700&display=swap">
<style>
  :root {
    --backdrop: #2b2b2b;
    --paper: #ffffff;
    --brand-red: #d81d1d;
    --deep-red: #b30d0d;
    --band-grey: #5e5e5e;
    --band-grey-light: #8a8a8a;
    --accent-cyan: #2fd6e4;
    --ink: #1c1c1c;
    --white: #ffffff;
  }
  * { box-sizing: border-box; margin: 0; padding: 0; }
  html, body { width: 907px; height: 1200px; overflow: hidden; background: var(--backdrop); }
  .canvas {
    position: relative; width: 907px; height: 1200px; overflow: hidden;
    font-family: "PT Serif", Georgia, serif; font-weight: 700;
  }
  .flyer-shapes, .hero-photo { position: absolute; left: 0; top: 0; }
  .text { position: absolute; white-space: nowrap; line-height: 1; }
  .right { text-align: right; }

  .brand-name { left: 560px; top: 212px; width: 270px; text-align: center; font-size: 31px; color: var(--ink); font-weight: 400; letter-spacing: 0.5px; }
  .brand-tagline { left: 560px; top: 250px; width: 270px; text-align: center; font-size: 11.5px; color: var(--ink); letter-spacing: 0.2px; }

  .headline-1 { left: 95px; top: 541px; font-size: 44px; color: var(--white); }
  .headline-2 { left: 95px; top: 588px; font-size: 31px; color: var(--white); }
  .headline-3 { left: 95px; top: 622px; font-size: 48px; color: var(--white); }
  .offer-lead { left: 89px; top: 692px; font-size: 24px; color: #f2f2f2; }
  .offer-amount { left: 89px; top: 724px; font-size: 33px; color: var(--accent-cyan); }

  .free-service { right: 76px; top: 767px; font-size: 37px; color: var(--accent-cyan); font-weight: 400; }
  .mobile-broker { right: 79px; top: 820px; font-size: 25px; color: var(--white); }
  .fine-print { right: 79px; top: 854px; width: 600px; font-size: 13.4px; line-height: 18px; color: var(--white); font-weight: 400; white-space: normal; text-align: right; }

  .contact-list { position: absolute; left: 80px; top: 960px; list-style: none; }
  .contact-list li { display: flex; align-items: center; height: 34px; font-size: 24px; color: var(--brand-red); }
  .contact-list svg { width: 16px; height: 16px; margin-right: 15px; flex: none; }

  .charity { position: absolute; left: 560px; top: 944px; width: 270px; text-align: center; color: var(--accent-cyan); }
  .charity-lead { font-size: 37px; font-weight: 400; line-height: 38px; }
  .charity-sub { font-size: 18px; line-height: 24px; }
  .charity-name { font-size: 27px; line-height: 30px; }
</style>
</head>
<body>
<div class="canvas">
  <svg class="flyer-shapes" width="907" height="1200" viewBox="0 0 907 1200" aria-hidden="true">
    <defs>
      <linearGradient id="greyBand" x1="0" x2="1" y1="0" y2="0">
        <stop offset="0" stop-color="var(--band-grey)"/>
        <stop offset="1" stop-color="var(--band-grey-light)"/>
      </linearGradient>
      <linearGradient id="redPanel" x1="0" x2="1" y1="0" y2="0">
        <stop offset="0" stop-color="var(--brand-red)"/>
        <stop offset="1" stop-color="var(--deep-red)"/>
      </linearGradient>
    </defs>
    <rect class="flyer-sheet" x="43" y="72" width="824" height="1058" fill="var(--paper)"/>
    <polygon class="corner-band-top" points="618,72 867,72 867,132" fill="var(--brand-red)"/>
    <polygon class="photo-edge-right" points="817,330 830,334 830,692 817,692" fill="var(--brand-red)"/>
    <polygon class="photo-edge-bottom" points="43,448 830,690 830,700 43,462" fill="var(--brand-red)"/>
    <polygon class="red-panel" points="75,825 812,700 867,712 867,1130 845,1130" fill="url(#redPanel)"/>
    <polygon class="grey-band" points="75,470 817,700 75,825" fill="url(#greyBand)"/>
    <polygon class="panel-shadow" points="75,825 845,1130 826,1130 75,838" fill="#111"/>
    <polygon class="corner-band-bottom" points="43,1045 290,1130 43,1130" fill="var(--brand-red)"/>
  </svg>

  <svg class="hero-photo" width="907" height="1200" viewBox="0 0 907 1200" role="img" aria-label="Photo of a modern white single-storey home with a tiled roof, manicured shrubs and tropical garden under a blue sky">
    <defs>
      <linearGradient id="photoTones" x1="0" y1="0" x2="0.6" y2="1">
        <stop offset="0" stop-color="#a9cde8"/>
        <stop offset="0.35" stop-color="#e8ecef"/>
        <stop offset="0.65" stop-color="#cfd6d4"/>
        <stop offset="1" stop-color="#4f8a3a"/>
      </linearGradient>
    </defs>
    <polygon points="43,98 817,342 817,690 43,450" fill="url(#photoTones)"/>
  </svg>

  <div class="text brand-name">Keel Lending</div>
  <div class="text brand-tagline">IS YOUR MORTGAGE IN GOOD SHAPE?</div>

  <div class="text headline-1">Get your</div>
  <div class="text headline-2">Mortgage in shape</div>
  <div class="text headline-3">for Summer</div>
  <div class="text offer-lead">Refinance today and potentially receive</div>
  <div class="text offer-amount">upwards of $1,500*</div>

  <div class="text right free-service">100% free service</div>
  <div class="text right mobile-broker">Mobile broker to your door, at your convenience</div>
  <p class="text fine-print">Re-finance before 2015 and not only will your Mortgage specialist find you a better product, but they will also rebate you 50% of their brokering commission. An average $500,000 loan is likely to result in over $1,500 cash back. Has there ever been a better reason to refinance?</p>

  <ul class="contact-list">
    <li>
      <svg viewBox="0 0 16 16" aria-hidden="true"><rect x="4" y="1" width="8" height="14" rx="1" fill="var(--ink)"/><rect x="5.5" y="3" width="5" height="5" fill="#fff"/></svg>
      0400 382 947
    </li>
    <li>
      <svg viewBox="0 0 16 16" aria-hidden="true"><rect x="2" y="4" width="12" height="8" fill="var(--ink)"/><polyline points="2,4 8,9 14,4" fill="none" stroke="#fff" stroke-width="1"/></svg>
      oscar@keellending.com.au
    </li>
    <li>
      <svg viewBox="0 0 16 16" aria-hidden="true"><circle cx="8" cy="8" r="6.5" fill="var(--ink)"/><path d="M1.5 8h13M8 1.5v13M3 4.5h10M3 11.5h10" stroke="#fff" stroke-width="0.8" fill="none"/></svg>
      www.keellending.com.au
    </li>
  </ul>

  <div class="charity">
    <div class="charity-lead">5% of profits</div>
    <div class="charity-sub">donated to our partner</div>
    <div class="charity-name">bright harbour</div>
  </div>
</div>
</body>
</html>
```